Brightpath, LLC
Electrical Contracting Company
We really like the back of #125 & #126 and the logo design on the front of #125.
We liked the front layout of #122, and we especially liked how they included the phrase Electrical Contracting Company on the card.
#118 we really like the front and back of your card. We like the colors, we like the shadowing.
We like the symbols for phone, cell, etc.
The above info was updated in the brief summary.
Please not changes to information:
instead of Electrical Contracting Corporation it needs to be Electrical Contracting Company
And the Fax number is 612-437-2908

```html
<!DOCTYPE html>
<html lang="en">
<head>
<meta charset="utf-8">
<title>Brightpath, LLC — Stationery Set</title>
<link rel="stylesheet" href="https://fonts.googleapis.com/css2?family=Open+Sans:wght@400;600;700&display=swap">
<style>
  :root {
    --backdrop: #e9e8e6;
    --paper: #ffffff;
    --ink: #2f2f2f;
    --ink-soft: #6b6b6b;
    --rule: #9a9a9a;
    --ghost: #f1f1f1;
    --edge: #d6d6d6;
  }
  * { box-sizing: border-box; margin: 0; padding: 0; }
  html, body { width: 1200px; height: 595px; overflow: hidden; }
  body {
    background: var(--backdrop);
    font-family: "Open Sans", Arial, sans-serif;
    color: var(--ink);
    position: relative;
  }
  .sheet {
    position: absolute;
    background: var(--paper);
    border: 1px solid var(--edge);
    overflow: hidden;
  }
  .letterhead { left: 12px; top: 48px; width: 372px; height: 538px; }
  .fax-sheet  { left: 396px; top: 48px; width: 372px; height: 538px; }
  .card-front { left: 804px; top: 53px; width: 146px; height: 94px; border-radius: 4px; }
  .card-back  { left: 962px; top: 163px; width: 156px; height: 96px; border-radius: 4px; }
  .envelope-back  { left: 776px; top: 298px; width: 412px; height: 136px; }
  .envelope-front { left: 776px; top: 446px; width: 412px; height: 140px; }

  /* brand mark stand-in */
  .brand { position: absolute; display: flex; flex-direction: column; align-items: center; }
  .brand-dot { border-radius: 50%; border: 1.5px solid var(--ink); }
  .brand-name { font-weight: 700; color: var(--ink); white-space: nowrap; }

  .sheet-header .brand { left: 14px; top: 14px; }
  .sheet-header .brand-dot { width: 20px; height: 20px; margin-bottom: 4px; }
  .sheet-header .brand-name { font-size: 6.5px; }
  .header-divider { position: absolute; left: 80px; top: 16px; width: 1px; height: 32px; background: var(--rule); }
  .header-col { position: absolute; top: 20px; font-size: 5.5px; line-height: 10px; color: var(--ink-soft); }
  .header-col.address { left: 90px; }
  .header-col.phones { left: 180px; }
  .header-col.web { left: 262px; }
  .contact-line { display: flex; align-items: center; gap: 4px; white-space: nowrap; }
  .contact-line svg { width: 6px; height: 6px; flex: none; }

  .ghost-mark {
    position: absolute; left: 50%; transform: translateX(-50%);
    width: 120px; height: 120px; border-radius: 50%;
    border: 3px solid var(--ghost);
  }
  .letterhead .ghost-mark, .fax-sheet .ghost-mark { top: 262px; }

  .fax-title { position: absolute; top: 76px; width: 100%; text-align: center; font-size: 15px; font-weight: 600; }
  .fax-table {
    position: absolute; left: 22px; top: 100px; width: 328px;
    border-collapse: collapse; font-size: 5.5px; color: var(--ink-soft);
  }
  .fax-table td { border: 1px solid var(--rule); height: 17px; padding: 0 4px; }
  .fax-table td.label { width: 36px; }
  .fax-options {
    position: absolute; left: 22px; top: 180px; width: 328px; height: 14px;
    border: 1px solid var(--rule); display: flex; justify-content: space-around; align-items: center;
    font-size: 5px; color: var(--ink-soft);
  }
  .fax-options span { display: flex; align-items: center; gap: 3px; }
  .fax-options i { width: 5px; height: 5px; border: 1px solid var(--rule); display: inline-block; }

  .card-front .brand { left: 10px; top: 12px; }
  .card-front .brand-dot { width: 20px; height: 20px; margin-bottom: 3px; }
  .card-front .brand-name { font-size: 5.5px; }
  .card-front .card-divider { position: absolute; left: 64px; top: 12px; width: 1px; height: 66px; background: var(--rule); }
  .card-details { position: absolute; left: 72px; top: 12px; font-size: 4.5px; line-height: 8px; color: var(--ink-soft); }
  .card-details .person { font-size: 6px; font-weight: 700; color: var(--ink); line-height: 8px; }
  .card-details .role { margin-bottom: 6px; }

  .card-back .brand { left: 50%; top: 18px; transform: translateX(-50%); }
  .card-back .brand-dot { width: 30px; height: 30px; margin-bottom: 4px; }
  .card-back .brand-name { font-size: 6.5px; }
  .card-back .tagline { position: absolute; top: 66px; width: 100%; text-align: center; font-size: 4.5px; color: var(--ink-soft); }
  .card-back .site { position: absolute; top: 78px; width: 100%; text-align: center; font-size: 5px; color: var(--ink-soft); }

  .envelope-flap { position: absolute; left: 0; top: 0; width: 100%; height: 100%; }
  .envelope-back .brand { left: 50%; top: 6px; transform: translateX(-50%); }
  .envelope-back .brand-dot { width: 22px; height: 22px; margin-bottom: 3px; background: var(--paper); }
  .envelope-back .brand-name { font-size: 6px; background: var(--paper); padding: 0 2px; }

  .envelope-front .brand { left: 14px; top: 12px; }
  .envelope-front .brand-dot { width: 20px; height: 20px; margin-bottom: 3px; }
  .envelope-front .brand-name { font-size: 6px; }
  .return-address { position: absolute; left: 14px; top: 104px; font-size: 5.5px; line-height: 9px; color: var(--ink-soft); }
</style>
</head>
<body>

<svg width="0" height="0" style="position:absolute">
  <defs>
    <symbol id="icon-phone" viewBox="0 0 10 10">
      <path d="M2 1h2l1 2.5-1.3 1a6 6 0 0 0 2.8 2.8l1-1.3L10 7v2a1 1 0 0 1-1 1A9 9 0 0 1 0 2a1 1 0 0 1 1-1z" fill="#6b6b6b"/>
    </symbol>
    <symbol id="icon-fax" viewBox="0 0 10 10">
      <rect x="2.5" y="0.5" width="5" height="3" fill="none" stroke="#6b6b6b"/>
      <rect x="0.5" y="3.5" width="9" height="4.5" fill="#6b6b6b"/>
      <rect x="2.5" y="6.5" width="5" height="3" fill="#fff" stroke="#6b6b6b"/>
    </symbol>
    <symbol id="icon-mail" viewBox="0 0 10 10">
      <rect x="0.5" y="2" width="9" height="6.5" fill="none" stroke="#6b6b6b"/>
      <path d="M0.5 2l4.5 4 4.5-4" fill="none" stroke="#6b6b6b"/>
    </symbol>
    <symbol id="icon-web" viewBox="0 0 10 10">
      <circle cx="5" cy="5" r="4.3" fill="none" stroke="#6b6b6b"/>
      <path d="M0.7 5h8.6M5 0.7c-2.4 2.6-2.4 6 0 8.6M5 0.7c2.4 2.6 2.4 6 0 8.6" fill="none" stroke="#6b6b6b" stroke-width="0.8"/>
    </symbol>
  </defs>
</svg>

<!-- Letterhead -->
<section class="sheet letterhead">
  <header class="sheet-header">
    <div class="brand"><span class="brand-dot"></span><span class="brand-name">Brightpath, LLC</span></div>
    <div class="header-divider"></div>
    <div class="header-col address"><div>136 Elmwood Rd</div><div>Eastonville, NY 10458</div></div>
    <div class="header-col phones">
      <div class="contact-line"><svg><use href="#icon-phone"/></svg>612-437-2931</div>
      <div class="contact-line"><svg><use href="#icon-fax"/></svg>612-437-2908</div>
    </div>
    <div class="header-col web">
      <div class="contact-line"><svg><use href="#icon-mail"/></svg>contact@marlowtide.com</div>
      <div class="contact-line"><svg><use href="#icon-web"/></svg>www.marlowtide.com</div>
    </div>
  </header>
  <div class="ghost-mark" aria-hidden="true"></div>
</section>

<!-- Fax sheet -->
<section class="sheet fax-sheet">
  <header class="sheet-header">
    <div class="brand"><span class="brand-dot"></span><span class="brand-name">Brightpath, LLC</span></div>
    <div class="header-divider"></div>
    <div class="header-col address"><div>136 Elmwood Rd</div><div>Eastonville, NY 10458</div></div>
    <div class="header-col phones">
      <div class="contact-line"><svg><use href="#icon-phone"/></svg>612-437-2931</div>
      <div class="contact-line"><svg><use href="#icon-fax"/></svg>612-437-2908</div>
    </div>
    <div class="header-col web">
      <div class="contact-line"><svg><use href="#icon-mail"/></svg>contact@marlowtide.com</div>
      <div class="contact-line"><svg><use href="#icon-web"/></svg>www.marlowtide.com</div>
    </div>
  </header>
  <h1 class="fax-title">Fax Sheet</h1>
  <table class="fax-table">
    <tr><td class="label">To:</td><td></td><td class="label">From:</td><td></td></tr>
    <tr><td class="label">Fax:</td><td></td><td class="label">Pages:</td><td></td></tr>
    <tr><td class="label">Phone:</td><td></td><td class="label">Date:</td><td></td></tr>
    <tr><td class="label">Re:</td><td></td><td class="label">CC:</td><td></td></tr>
  </table>
  <div class="fax-options">
    <span><i></i>Urgent</span>
    <span><i></i>For Review</span>
    <span><i></i>Please Comment</span>
    <span><i></i>Please Reply</span>
    <span><i></i>Please Recycle</span>
  </div>
  <div class="ghost-mark" aria-hidden="true"></div>
</section>

<!-- Business card, front -->
<section class="sheet card-front">
  <div class="brand"><span class="brand-dot"></span><span class="brand-name">Brightpath, LLC</span></div>
  <div class="card-divider"></div>
  <div class="card-details">
    <div class="person">Dana Reyes</div>
    <div class="role">Owner</div>
    <div class="contact-line"><svg><use href="#icon-phone"/></svg>612-437-2931</div>
    <div class="contact-line"><svg><use href="#icon-fax"/></svg>612-437-2908</div>
    <div class="contact-line"><svg><use href="#icon-mail"/></svg>dana@marlowtide.com</div>
    <div class="contact-line"><svg><use href="#icon-web"/></svg>marlowtide.com</div>
  </div>
</section>

<!-- Business card, back -->
<section class="sheet card-back">
  <div class="brand"><span class="brand-dot"></span><span class="brand-name">Brightpath, LLC</span></div>
  <div class="tagline">Electrical Contracting Company</div>
  <div class="site">www.marlowtide.com</div>
</section>

<!-- Envelope, back -->
<section class="sheet envelope-back">
  <svg class="envelope-flap" viewBox="0 0 412 136" preserveAspectRatio="none" aria-hidden="true">
    <polyline points="0,0 206,52 412,0" fill="none" stroke="#9a9a9a" stroke-width="1"/>
  </svg>
  <div class="brand"><span class="brand-dot"></span><span class="brand-name">Brightpath, LLC</span></div>
</section>

<!-- Envelope, front -->
<section class="sheet envelope-front">
  <div class="brand"><span class="brand-dot"></span><span class="brand-name">Brightpath, LLC</span></div>
  <div class="return-address"><div>136 Elmwood Rd</div><div>Eastonville, NY 10458</div></div>
</section>

</body>
</html>
```